New Alcoholic Spiked Seltzer Line

We need a can design for a line of low calorie alcoholic seltzer. This product is a sparkling water and vodka drink with no sugar added in a slim 12 oz can.

This is a lighter, healthier, alternative to the sugary ready-to-drinks on the market. The product contains only 3 ingredients: Vodka, Water and Natural Flavors. It has only 100 calories but still has 5% alcohol, so you don't need to sacrifice alcohol to cut calories.

This product also does not contain any preservatives.

We want this design to communicate the following objectives to the consumer and in this order:

1. Appetizing product
2.Low calorie
3.Communicate the type of beverage (Spiked Seltzer)

The brand name of the product is VELKA.

The flavor of the product needed to be used for the design is Mango-Orange.

Comparable products are:

www.brisavelfizz.example/
https://www.tarnowbubble.example
https://quellrind.example/

The designs should not infringe or copy the creative directions of the products mentionned above. They are only given so that you can better understand the type of product we are developing.

Target Market(s)

Young Professional women between the ages of 25 and 44

Industry/Entity Type

Product

Colors

Designer to choose colors to be used in the design.

Requirements
Must have
• Design extendibility, meaning it can be adapted for other flavors.
• This is a new category in the market we are targeting, so consumers must easily be able to identify what type of product this is.

```html
<!DOCTYPE html>
<html lang="en">
<head>
<meta charset="utf-8">
<title>VELKA Spiked Seltzer – Mango-Orange Label</title>
<link href="https://fonts.googleapis.com/css2?family=Ubuntu:wght@300;400;700&display=swap" rel="stylesheet">
<style>
  :root {
    --bg: #e4e4e4;
    --orange-light: #f8b040;
    --orange: #f4a027;
    --orange-deep: #ee931c;
    --ink: #2b1710;
    --ink-soft: #4a2a18;
  }
  html, body {
    margin: 0;
    padding: 0;
    width: 1200px;
    height: 1200px;
    overflow: hidden;
    background: var(--bg);
  }
  .canvas {
    position: relative;
    width: 1200px;
    height: 1200px;
    background: var(--bg);
  }
  .label {
    position: absolute;
    left: 462px;
    top: 216px;
    width: 330px;
    height: 832px;
    background: linear-gradient(90deg, var(--orange-light) 0%, var(--orange) 45%, var(--orange-deep) 100%);
    color: var(--ink);
    font-family: "Ubuntu", sans-serif;
  }
  .brand {
    position: absolute;
    left: 22px;
    top: 188px;
    width: 96px;
    height: 476px;
  }
  .brand span {
    position: absolute;
    left: 50%;
    top: 50%;
    transform: translate(-50%, -50%) rotate(-90deg);
    font-family: "Ubuntu", sans-serif;
    font-weight: 400;
    font-size: 128px;
    line-height: 1;
    letter-spacing: 14px;
    padding-left: 14px;
    white-space: nowrap;
    color: var(--ink);
  }
  .info {
    position: absolute;
    left: 148px;
    top: 0;
    width: 176px;
    height: 100%;
  }
  .category {
    position: absolute;
    top: 184px;
    left: 0;
    margin: 0;
    font-weight: 400;
    font-size: 40px;
    line-height: 50px;
    white-space: nowrap;
  }
  .rule {
    position: absolute;
    left: 0;
    width: 174px;
    height: 2px;
    background: var(--ink);
  }
  .rule--top { top: 294px; }
  .rule--mid { top: 430px; }
  .abv {
    position: absolute;
    left: 0;
    top: 300px;
    width: 174px;
    height: 124px;
  }
  .abv__num {
    position: absolute;
    left: 2px;
    top: 0;
    font-weight: 300;
    font-size: 128px;
    line-height: 124px;
  }
  .abv__pct {
    position: absolute;
    left: 74px;
    top: 10px;
    font-weight: 300;
    font-size: 58px;
    line-height: 58px;
  }
  .abv__unit {
    position: absolute;
    left: 78px;
    top: 88px;
    font-weight: 300;
    font-size: 15px;
    white-space: nowrap;
    color: var(--ink-soft);
  }
  .recipe {
    position: absolute;
    top: 442px;
    left: 3px;
    font-weight: 300;
    font-size: 15px;
    white-space: nowrap;
    color: var(--ink-soft);
  }
  .plus {
    position: absolute;
    top: 470px;
    left: 2px;
    font-weight: 300;
    font-size: 13px;
    color: var(--ink-soft);
  }
  .flavor {
    position: absolute;
    top: 494px;
    left: 0;
    margin: 0;
    font-weight: 700;
    font-size: 36px;
    line-height: 48px;
    white-space: nowrap;
    letter-spacing: -0.5px;
  }
  .claims {
    position: absolute;
    top: 600px;
    left: 0;
    margin: 0;
    padding: 0;
    list-style: none;
    font-weight: 300;
    font-size: 16px;
    line-height: 24px;
    white-space: nowrap;
    color: var(--ink-soft);
  }
</style>
</head>
<body>
  <div class="canvas">
    <section class="label" aria-label="VELKA Spiked Seltzer Mango-Orange can label">
      <div class="brand"><span>VELKA</span></div>
      <div class="info">
        <h2 class="category">Spiked<br>Seltzer</h2>
        <div class="rule rule--top"></div>
        <div class="abv">
          <span class="abv__num">5</span>
          <span class="abv__pct">%</span>
          <span class="abv__unit">Alc. Vol.</span>
        </div>
        <div class="rule rule--mid"></div>
        <div class="recipe">Vodka mixed with Water</div>
        <div class="plus">+</div>
        <h1 class="flavor">Mango -<br>Orange</h1>
        <ul class="claims">
          <li>100 calories</li>
          <li>Natural Flavor</li>
          <li>No preservatives</li>
        </ul>
      </div>
    </section>
  </div>
</body>
</html>
```